Business Card Design

We need a business card designed which uses our logo and looks really good. The company is called Veltramor482. We help e-commerce companies reduce cart abandonment by rescuing the sale through our innovative technology.

Our corporate colors are red, black and white.

I have attached our AI file for the logo as well.

Additional information for the business card:

Name: Marcus Delby
Title: President/CTO
Phone: 1-877-VELT-482
Website: www.veltramor482.com
Email: marcus@veltramor482.com

Tag line: Bringing Every Cart Home

Industry/Entity Type

E-Commerce

```html
<!DOCTYPE html>
<html lang="en">
<head>
<meta charset="utf-8">
<title>Veltramor482 Business Card</title>
<link rel="stylesheet" href="https://fonts.googleapis.com/css2?family=Lato:wght@300;400&display=swap">
<style>
  :root {
    --page-bg: #e6e3de;
    --card-bg: #f4f4f2;
    --brand-red: #a5161f;
    --ink-dark: #2c2c2c;
    --ink-grey: #6a6a6a;
    --ink-soft: #7a7a7a;
    --rule-red: #b3343a;
  }
  html, body {
    margin: 0;
    padding: 0;
    width: 1200px;
    height: 848px;
    overflow: hidden;
    background: var(--page-bg);
    font-family: "Lato", "Helvetica Neue", Arial, sans-serif;
  }
  .card {
    position: absolute;
    left: 144px;
    top: 132px;
    width: 940px;
    height: 550px;
    background: var(--card-bg);
    border-radius: 30px;
    box-shadow: 0 2px 10px rgba(0,0,0,0.12);
    overflow: hidden;
  }
  .brand {
    position: absolute;
    left: 0;
    right: 0;
    top: 20px;
    display: flex;
    justify-content: center;
    align-items: center;
    gap: 12px;
  }
  .brand-dot {
    width: 22px;
    height: 22px;
    border-radius: 50%;
    background: var(--brand-red);
  }
  .brand-name {
    font-size: 42px;
    font-weight: 400;
    line-height: 1;
    letter-spacing: 0.5px;
    color: var(--ink-dark);
  }
  .tagline {
    position: absolute;
    left: 0;
    right: 0;
    top: 63px;
    margin: 0;
    text-align: center;
    font-size: 23px;
    font-weight: 300;
    line-height: 1;
    color: var(--ink-grey);
  }
  .rule {
    position: absolute;
    height: 1.5px;
    background: var(--rule-red);
  }
  .rule-left { left: 0; width: 318px; }
  .rule-right { left: 610px; right: 0; }
  .rule-upper { top: 247px; }
  .rule-lower { top: 336px; }
  .emblem-ring {
    position: absolute;
    left: 316px;
    top: 130px;
    width: 294px;
    height: 294px;
    border: 2.5px solid var(--brand-red);
    border-radius: 50%;
    box-sizing: border-box;
    background: var(--card-bg);
  }
  .contact {
    position: absolute;
    display: flex;
    align-items: center;
    gap: 9px;
    font-size: 19px;
    font-weight: 300;
    line-height: 1;
    color: var(--ink-grey);
    transform: translateY(-50%);
    white-space: nowrap;
  }
  .contact svg {
    width: 17px;
    height: 17px;
    flex: none;
  }
  .contact-web { left: 34px; top: 226px; }
  .contact-mail { left: 34px; top: 315px; }
  .contact-address { left: 626px; top: 224px; }
  .contact-phone { left: 631px; top: 315px; }
  .person-name {
    position: absolute;
    left: 0;
    right: 0;
    top: 477px;
    text-align: center;
    font-size: 29px;
    font-weight: 300;
    line-height: 1;
    color: var(--brand-red);
  }
  .person-title {
    position: absolute;
    left: 0;
    right: 0;
    top: 513px;
    text-align: center;
    font-size: 17px;
    font-weight: 400;
    line-height: 1;
    letter-spacing: 4px;
    color: var(--ink-soft);
  }
</style>
</head>
<body>
  <section class="card">
    <header class="brand">
      <span class="brand-dot"></span>
      <span class="brand-name">Veltramor482</span>
    </header>
    <p class="tagline">Bringing Every Cart Home</p>

    <div class="rule rule-left rule-upper"></div>
    <div class="rule rule-left rule-lower"></div>
    <div class="rule rule-right rule-upper"></div>
    <div class="rule rule-right rule-lower"></div>

    <div class="emblem-ring"></div>

    <div class="contact contact-web">
      <svg viewBox="0 0 16 16" aria-hidden="true"><path d="M15 1 1 7l6 2 2 6z" fill="var(--brand-red)"/></svg>
      <span>www.veltramor482.com</span>
    </div>
    <div class="contact contact-mail">
      <svg viewBox="0 0 16 16" aria-hidden="true"><rect x="1" y="3" width="14" height="10" fill="none" stroke="var(--brand-red)" stroke-width="1.5"/><path d="M1 3l7 6 7-6M1 13l5-5M15 13l-5-5" fill="none" stroke="var(--brand-red)" stroke-width="1.2"/></svg>
      <span>info@veltramor482.com</span>
    </div>
    <div class="contact contact-address">
      <svg viewBox="0 0 16 16" aria-hidden="true" style="width:12px"><path d="M8 1c2.5 0 3.5 2 3.5 3.5C11.5 7 8 15 8 15S4.5 7 4.5 4.5C4.5 3 5.5 1 8 1z" fill="var(--brand-red)"/></svg>
      <span>318 Harlow St Brenton, NY 10482</span>
    </div>
    <div class="contact contact-phone">
      <svg viewBox="0 0 16 16" aria-hidden="true"><rect x="1.5" y="1.5" width="13" height="13" rx="1" fill="none" stroke="var(--brand-red)" stroke-width="1.4"/><path d="M5 4h2l.6 2-1 1c.6 1.2 1.2 1.8 2.4 2.4l1-1 2 .6v2c-4 .3-7.2-2.9-7-7z" fill="var(--brand-red)"/></svg>
      <span>1-877-VELT-482 (Toll Free)</span>
    </div>

    <div class="person-name">Marcus Delby</div>
    <div class="person-title">President/CTO</div>
  </section>
</body>
</html>
```